CPA Firm Stationary & Business Cards
Whitfield & Partners CPAs PSC
CPA Firm Stationary & Business Cards - Financial Services
Creative Brief
Professional
Martin L. Dowse, CPA
Shareholder
4815 Tillamore Ave. Suite 1 Halden Ridge, KY 40999
mdowse@wpfcpa.net
www.wpfcpa.net
We are a CPA (Certified Public Accountant) firm, in business since 1924. In addition to Business Cards, I would also like to see designs for Letterheads and Envelopes.
Your choice. At a minimum, it should include the "W" logo.In addition to Business Cards, I would also like to see designs for Letterheads and Envelopes.

```html
<!DOCTYPE html>
<html lang="en">
<head>
<meta charset="utf-8">
<title>Whitfield &amp; Partners CPAs PSC – Business Cards</title>
<link href="https://fonts.googleapis.com/css2?family=Montserrat:wght@400;600;700&display=swap" rel="stylesheet">
<style>
  :root {
    --page: #e9eaec;
    --card-white: #ffffff;
    --ink: #3a3f47;
    --ink-soft: #6b717a;
    --brand-blue: #1d5fc9;
    --brand-blue-deep: #163e9c;
    --brand-blue-light: #2f8de0;
    --band-grey: #8e9298;
    --band-grey-light: #b7babf;
  }
  * { margin: 0; padding: 0; box-sizing: border-box; }
  html, body { width: 1200px; height: 901px; overflow: hidden; }
  body {
    background: var(--page);
    font-family: "Montserrat", Arial, sans-serif;
    display: flex;
    align-items: center;
    justify-content: center;
    gap: 60px;
  }
  .card {
    position: relative;
    width: 520px;
    height: 300px;
    border-radius: 14px;
    overflow: hidden;
    box-shadow: 0 10px 28px rgba(0,0,0,0.18);
  }
  .card-front { background: var(--card-white); }
  .card-front .shapes { position: absolute; inset: 0; }
  .firm-mark {
    position: absolute; left: 30px; top: 40px;
    display: flex; align-items: center; gap: 10px;
  }
  .firm-mark .dot {
    width: 22px; height: 22px; border-radius: 50%;
    background: var(--brand-blue);
    flex-shrink: 0;
  }
  .firm-name {
    color: var(--brand-blue);
    font-weight: 700;
    font-size: 15px;
    letter-spacing: 0.5px;
    line-height: 1.2;
    width: 170px;
  }
  .address {
    position: absolute; left: 30px; top: 128px;
    font-size: 9px; color: var(--ink-soft); line-height: 1.5;
  }
  .contacts {
    position: absolute; left: 30px; bottom: 28px;
    list-style: none;
    font-size: 8.5px; color: var(--ink-soft); line-height: 1.75;
  }
  .contacts li { display: flex; align-items: center; gap: 7px; }
  .contacts .icon {
    width: 9px; height: 9px; border-radius: 2px; background: var(--brand-blue);
    flex-shrink: 0;
  }
  .person {
    position: absolute; right: 22px; top: 200px;
    color: var(--card-white); text-align: right;
  }
  .person-name { font-weight: 600; font-size: 13px; white-space: nowrap; }
  .person-title { font-size: 8.5px; opacity: 0.85; margin-top: 3px; }
  .card-back {
    background: linear-gradient(160deg, var(--brand-blue-deep) 0%, var(--brand-blue) 55%, var(--brand-blue-light) 100%);
    display: flex; align-items: center; justify-content: center;
  }
  .back-name {
    color: var(--card-white);
    font-weight: 700;
    font-size: 20px;
    letter-spacing: 1px;
    text-align: center;
    line-height: 1.3;
  }
</style>
</head>
<body>
  <section class="card card-front" aria-label="Business card front">
    <svg class="shapes" viewBox="0 0 520 300" preserveAspectRatio="none">
      <defs>
        <linearGradient id="greyBand" x1="0" y1="0" x2="1" y2="1">
          <stop offset="0" stop-color="#b7babf"/>
          <stop offset="1" stop-color="#8e9298"/>
        </linearGradient>
        <linearGradient id="blueBand" x1="0" y1="0" x2="1" y2="1">
          <stop offset="0" stop-color="#2f8de0"/>
          <stop offset="1" stop-color="#163e9c"/>
        </linearGradient>
      </defs>
      <path d="M215 0 H520 V300 H250 C330 200 310 60 215 0 Z" fill="url(#greyBand)"/>
      <path d="M520 30 C400 80 300 180 250 300 H520 Z" fill="url(#blueBand)"/>
    </svg>
    <div class="firm-mark">
      <span class="dot"></span>
      <span class="firm-name">Whitfield &amp; Partners CPAs PSC</span>
    </div>
    <p class="address">4815 Tillamore Ave.<br>Suite 1<br>Halden Ridge, KY 40999</p>
    <ul class="contacts">
      <li><span class="icon"></span>P 270.555.0142</li>
      <li><span class="icon"></span>F 270.555.0143</li>
      <li><span class="icon"></span>mdowse@wpfcpa.net</li>
      <li><span class="icon"></span>www.wpfcpa.net</li>
    </ul>
    <div class="person">
      <p class="person-name">Martin L. Dowse, CPA</p>
      <p class="person-title">Shareholder</p>
    </div>
  </section>

  <section class="card card-back" aria-label="Business card back">
    <p class="back-name">Whitfield &amp; Partners<br>CPAs PSC</p>
  </section>
</body>
</html>
```